Re-design my 1-page website to be BETTER!

Hi Guys,
I recently created a 1-page website for market testing purposes for a company I am starting. Problem is, the feedback i've had on the page is its a bit corporate and boring.
I would love you to design something that is fresher, more modern and will generate leads (via the sign up CTA's).
Here is the website as it is now: www.guidelinkhub.com.au.
If you need any info or have questions, just reach out.
Thanks,
Oliver

Target Market(s)

Entrepreneurs

Number of Pages Required

1 page

Font styles to use
Sans Serif

Colors
abd036
34a6d7
ffffff

Requirements
Must have
• Fresh, Modern, high-converting
• I expect 70% of traffic to be mobile so must be mobile optimised first.
Nice to have
• I've highlighted colours i like below, however, I am open to suggestions. I like colours that are gender neutral and show energy and vibrancy.
• I have used Proxima Nova for the fonts, as I find it easy to read however, I am open to suggestions. My main preference is that it displays well and is easily read

```html
<!DOCTYPE html>
<html lang="en">
<head>
<meta charset="utf-8">
<title>GuideLink Hub – A Mentor for Everyone</title>
<link href="https://fonts.googleapis.com/css2?family=Poppins:ital,wght@0,300;0,400;0,500;0,600;1,300&display=swap" rel="stylesheet">
<style>
:root{
  --green:#abd036;
  --blue:#34a6d7;
  --white:#ffffff;
  --ink:#3a3a3a;
  --text:#444;
  --muted:#666;
}
*{box-sizing:border-box;margin:0;padding:0}
html,body{width:1200px;height:4412px;overflow:hidden}
body{position:relative;background:var(--white);font-family:'Poppins',sans-serif;color:var(--text)}
.abs{position:absolute}
.btn{position:absolute;display:flex;align-items:center;justify-content:center;background:var(--blue);color:var(--white);border-radius:20px;font-size:10px;font-weight:500;box-shadow:0 3px 8px rgba(52,166,215,.3)}
.brand{font-weight:600;color:var(--blue);font-size:21px}
.heading{position:absolute;left:0;width:1200px;text-align:center;font-size:26px;font-weight:500;color:var(--ink)}
.rule{position:absolute;left:575px;width:50px;height:4px;background:var(--green);border-radius:2px}

.site-header{position:absolute;top:0;left:0;width:1200px;height:80px;background:var(--white)}
.hero{position:absolute;top:80px;left:0;width:1200px;height:500px;overflow:hidden}
.hero-photo{position:absolute;inset:0;background:linear-gradient(110deg,#5f7388 0%,#8fa0ae 35%,#b7c2c9 60%,#9aa7b0 100%)}
.hero-photo::after{content:"";position:absolute;inset:0;background:linear-gradient(90deg,rgba(30,50,70,.35),rgba(30,50,70,.05))}
.hero-title{left:212px;top:166px;font-size:42px;font-weight:500;color:var(--white);letter-spacing:-.5px}
.hero-sub{left:214px;top:220px;font-size:12px;color:var(--white)}

.quote{left:0;width:1200px;top:656px;text-align:center;font-size:26px;font-style:italic;font-weight:300;line-height:31px;color:var(--ink)}
.quote-by{left:656px;top:777px;font-size:15px;color:var(--blue)}

.intro-text{left:212px;top:1028px;width:436px;font-size:15.5px;line-height:23px;color:var(--text)}
.intro-text p{margin-bottom:22px}
.intro-photo{left:671px;top:1013px;width:322px;height:367px;border-radius:12px;background:linear-gradient(160deg,#c6d3dc,#6e8799 55%,#2f4a5e);border-bottom:5px solid var(--blue);border-right:5px solid var(--blue)}

.lead{left:0;width:1200px;top:1564px;text-align:center;font-size:15px;line-height:23px;color:var(--text)}
.card{position:absolute;top:1676px;width:250px;height:248px;background:var(--white);border-radius:8px;box-shadow:0 4px 14px rgba(0,0,0,.09);padding:50px 22px 0;text-align:center;border-bottom:4px solid;border-image:linear-gradient(90deg,var(--blue),var(--green)) 1}
.card.active{border:4px solid transparent;border-radius:8px;background:linear-gradient(#fff,#fff) padding-box,linear-gradient(135deg,var(--green),var(--blue)) border-box}
.card h3{font-size:15px;font-weight:500;color:var(--ink);margin-bottom:18px}
.card p{font-size:12.5px;line-height:19px;color:var(--muted)}

.growth{position:absolute;top:2140px;left:0;width:1200px;height:760px;overflow:hidden}
.growth-photo{position:absolute;inset:0;background:linear-gradient(120deg,#6b7882,#8e9aa2 40%,#6f7d86 70%,#4f5d66)}
.growth-photo::after{content:"";position:absolute;inset:0;background:rgba(35,50,60,.35)}
.growth-title{position:absolute;top:84px;width:1200px;text-align:center;font-size:26px;font-weight:500;color:var(--white)}
.benefit{position:absolute;width:250px;text-align:center;color:var(--white)}
.benefit svg{display:block;margin:0 auto 8px}
.benefit h4{font-size:16px;font-weight:400;margin-bottom:8px}
.benefit .bar{width:26px;height:3px;background:var(--green);margin:0 auto 12px}
.benefit p{font-size:10.5px;line-height:15px;padding:0 16px}
.benefit-glow{position:absolute;left:476px;top:175px;width:248px;height:248px;border-radius:8px;background:linear-gradient(160deg,rgba(171,208,54,.35),rgba(52,166,215,.35));border:2px solid rgba(171,208,54,.7)}

.faq-q{position:absolute;left:212px;width:382px;height:48px;border:2px solid var(--green);border-radius:10px;padding-left:16px;display:flex;align-items:center;font-size:15px;color:var(--ink);background:var(--white)}
.faq-q.open{background:var(--blue);border-color:var(--blue);color:var(--white);box-shadow:0 4px 10px rgba(0,0,0,.15)}
.faq-a{left:608px;top:3147px;width:380px;height:402px;border-radius:14px;background:linear-gradient(170deg,var(--blue) 0%,#6cbd9a 55%,var(--green) 100%);color:var(--white);padding:30px 30px 0;font-size:12.5px;line-height:19px}
.faq-a p{margin-bottom:15px}

.cta{position:absolute;top:3693px;left:0;width:1200px;height:510px;overflow:hidden}
.cta-photo{position:absolute;inset:0;background:linear-gradient(135deg,#5b6b76,#8797a1 50%,#a8b4bb)}
.cta-photo::after{content:"";position:absolute;inset:0;background:rgba(40,55,65,.45)}
.cta-title{position:absolute;top:116px;width:1200px;text-align:center;font-size:27px;font-weight:500;color:var(--white)}
.cta-text{position:absolute;top:200px;left:340px;width:520px;text-align:center;font-size:15.5px;line-height:23px;color:var(--white)}
.cta-text p{margin-bottom:18px}

.footer-note{top:4372px;font-size:10px;color:var(--muted)}
</style>
</head>
<body>

<header class="site-header">
  <div class="abs brand" style="left:212px;top:26px">GuideLink Hub</div>
  <div class="btn" style="left:861px;top:24px;width:127px;height:32px">Find my Mentor</div>
</header>

<section class="hero">
  <div class="hero-photo" role="img" aria-label="Photo of two young professionals laughing over a laptop on a sofa in a high-rise office"></div>
  <h1 class="abs hero-title">A Mentor for Everyone</h1>
  <div class="abs hero-sub">Free Registration. 100% Confidential. 100% Obligation Free</div>
  <div class="btn" style="left:212px;top:259px;width:149px;height:34px">Find my Mentor</div>
  <svg class="abs" style="left:0;top:390px" width="1200" height="110" viewBox="0 0 1200 110">
    <defs><linearGradient id="heroBand" x1="0" x2="1"><stop offset="0" stop-color="#34a6d7"/><stop offset="1" stop-color="#abd036"/></linearGradient></defs>
    <polygon points="0,60 1200,0 1200,12 0,72" fill="url(#heroBand)"/>
    <polygon points="0,72 1200,12 1200,110 0,110" fill="#fff"/>
  </svg>
</section>

<blockquote class="abs quote">"We've flipped the model on its head -  so now you<br>choose your Mentor.  It's never been this easy to<br>get the advice and guidance you need to thrive"</blockquote>
<div class="abs quote-by">Oliver, Founder - GuideLink Hub</div>

<h2 class="heading" style="top:896px">Finding a Mentor Has Never Been Easier</h2>
<div class="rule" style="top:943px"></div>

<div class="abs intro-text">
  <p>&nbsp;&nbsp;&nbsp;&nbsp;&nbsp;Having a great Mentor will turbo-charge your personal, professional or business growth.  But unless you have an incredible network, finding great Mentors has always been a challenge.</p>
  <p>GuideLink Hub changes all that, levelling the playing field and making it easy for entrepreneurs and professionals to find the advice and guidance they deserve.</p>
  <p>No longer will you have to go searching for your perfect Mentor.  We bring the perfect Mentor to you, selected from a global pool of experts, putting the power back in your hands and letting you get on with your growth.</p>
</div>
<div class="abs intro-photo" role="img" aria-label="Photo of a young man working on a laptop on a leather sofa by a city window"></div>

<h2 class="heading" style="top:1479px">Mentorship: But Different</h2>
<div class="abs lead">Finding a Mentor used to be hard; but not any more. We've turned<br>the traditional model on its head, so now Mentors seek you</div>

<div class="card" style="left:212px"><h3>Tell Us What You Need</h3><p>There is no one size fits all approach to Mentorship.  So tell us the challenges you are facing and the skill-set your Mentor must have.</p></div>
<div class="card active" style="left:476px"><h3>Choose Your Mentor</h3><p>Mentors are invited to Mentor you. We select 3 top picks that align with your criteria.  It's then up to you whether you choose a Mentor, interview 1 or more or refine your criteria and start again.</p></div>
<div class="card" style="left:738px"><h3>Ongoing Support</h3><p>We don't stop once you have your perfect Mentor.  We're on hand to make life easy for you, keep your sessions on track and provide ongoing support.</p></div>

<div class="btn" style="left:526px;top:1983px;width:149px;height:37px">Find my Mentor</div>

<section class="growth">
  <div class="growth-photo" role="img" aria-label="Photo of two men talking across a desk with laptops in a bright office"></div>
  <h2 class="growth-title">How a Mentor Will Accelerate Your Growth</h2>
  <div class="rule" style="top:131px"></div>
  <div class="benefit-glow"></div>

  <div class="benefit" style="left:212px;top:196px">
    <svg width="44" height="44" viewBox="0 0 44 44" fill="none" stroke="#fff" stroke-width="2"><circle cx="16" cy="14" r="8"/><path d="M6 40c0-8 4-14 10-14s10 6 10 14"/><path d="M30 8c3 3 3 9 0 12M35 4c5 5 5 15 0 20"/></svg>
    <h4>Impartial advice</h4><div class="bar"></div>
    <p>Imagine being able to speak to someone who has been through the challenges you are currently facing? Who has 'been there seen that' and can help you navigate the ups and downs of your career or business?</p>
  </div>
  <div class="benefit" style="left:476px;top:196px">
    <svg width="44" height="44" viewBox="0 0 44 44" fill="none" stroke="#fff" stroke-width="2"><circle cx="12" cy="30" r="8"/><circle cx="32" cy="30" r="8"/><path d="M8 22l3-16h6l1 16M36 22l-3-16h-6l-1 16M18 14h8"/></svg>
    <h4>Avoid the Pitfalls</h4><div class="bar"></div>
    <p>An experienced Mentor will help you see the challenges before they arise and make sure you avoid them altogether. Saving valuable time and money in the process.</p>
  </div>
  <div class="benefit" style="left:738px;top:196px">
    <svg width="44" height="44" viewBox="0 0 44 44" fill="none" stroke="#fff" stroke-width="2"><path d="M14 16a10 10 0 0 1 20 0c0 7-6 8-6 15a6 6 0 0 1-10 3"/><path d="M20 17a4 4 0 0 1 8 0c0 3-3 4-3 6"/><path d="M8 20c-2 3-2 7 0 10"/></svg>
    <h4>A Supportive Ear</h4><div class="bar"></div>
    <p>Running a business and the challenges of corporate life can be extremely stressful.  And often, our friends and family just don't get it.  So imagine having someone independent who can understand where your coming from and, help you see things objectively.</p>
  </div>

  <div class="benefit" style="left:212px;top:458px">
    <svg width="44" height="44" viewBox="0 0 44 44" fill="none" stroke="#fff" stroke-width="2"><circle cx="22" cy="22" r="18"/><path d="M12 16c4-2 6 2 10 0s6-4 10-2M10 26c5 0 7 4 12 2s8-2 12 0M22 4v36"/></svg>
    <h4>Clarity</h4><div class="bar"></div>
    <p>Sometimes we are so caught up in our own world we struggle to see the big picture.  You Mentor will provide an objective, outsider view.  Helping you to cut though the noise and focus on what's really important.</p>
  </div>
  <div class="benefit" style="left:476px;top:458px">
    <svg width="44" height="44" viewBox="0 0 44 44" fill="none" stroke="#fff" stroke-width="2"><circle cx="22" cy="9" r="5"/><path d="M22 14v12M14 20l8 4 8-4M8 34h28M12 40h20M16 26l-4 8M28 26l4 8"/></svg>
    <h4>Motivation</h4><div class="bar"></div>
    <p>Your Mentor has seen this before and been in your shoes.  They understand what your going through and will help you to re-focus and re-energise.</p>
  </div>
  <div class="benefit" style="left:738px;top:458px">
    <svg width="44" height="44" viewBox="0 0 44 44" fill="none" stroke="#fff" stroke-width="2"><path d="M22 4v36M10 10h22l4 5-4 5H10zM34 22H12l-4 5 4 5h22z"/></svg>
    <h4>Make you Accountable</h4><div class="bar"></div>
    <p>A Mentor is not just there to pick you up - they are to give honest appraisal and tell you when your falling short.  Ultimately, only you can control your success and you Mentor will hold you accountable to make sure you are.</p>
  </div>

  <svg class="abs" style="left:0;top:680px" width="1200" height="80" viewBox="0 0 1200 80">
    <defs><linearGradient id="growthBand" x1="0" x2="1"><stop offset="0" stop-color="#34a6d7"/><stop offset="1" stop-color="#abd036"/></linearGradient></defs>
    <polygon points="0,8 1200,48 1200,60 0,20" fill="url(#growthBand)"/>
    <polygon points="0,20 1200,60 1200,80 0,80" fill="#fff"/>
  </svg>
  <div class="btn" style="left:526px;top:705px;width:149px;height:35px">Find my Mentor</div>
</section>

<h2 class="heading" style="top:3006px">Frequently Asked Questions</h2>
<div class="rule" style="top:3053px"></div>

<div class="faq-q open" style="top:3147px">What is a Mentor?</div>
<div class="faq-q" style="top:3206px">Is a Mentor right for me?</div>
<div class="faq-q" style="top:3265px">How often do we meet?</div>
<div class="faq-q" style="top:3324px">Can I have more than one Mentor?</div>
<div class="faq-q" style="top:3383px">What if it doesn't work out?</div>
<div class="faq-q" style="top:3442px">How do we meet?</div>
<div class="faq-q" style="top:3501px">What are the costs?</div>

<div class="abs faq-a">
  <p>Experienced and Trusted Advisor.  Guru.<br>Confidente.  Friend.</p>
  <p>In essence a Mentor is someone who can turn to for guidance and advice.</p>
  <p>Someone who is more experienced than you and, has navigated similar challenges to you and can foresee the pitfalls and hurdles you face.</p>
  <p>A great Mentor is also a motivator, connector and guide.  Will help you focus on what's really important and see the bigger picture.</p>
  <p>Importantly, a great Mentor should be outside your immediate network of friends and relatives. And, be able to offer unbiased, honest and objective advice, that you can action.</p>
</div>

<section class="cta">
  <div class="cta-photo" role="img" aria-label="Photo of hands working at a laptop and notebook on a desk"></div>
  <h2 class="cta-title">It's Time to Invest in You</h2>
  <div class="cta-text">
    <p>If you've come this far you've already taken the most important step: recognising how mentorship can help you; and taking action to find it.</p>
    <p>And now your here, the rest is easy.</p>
    <p>Get started now and let GuideLink Hub do the rest...</p>
  </div>
  <div class="btn" style="left:526px;top:395px;width:149px;height:36px">Let`s Do This</div>
  <svg class="abs" style="left:0;top:492px" width="1200" height="18" viewBox="0 0 1200 18">
    <defs><linearGradient id="ctaBand" x1="0" x2="1"><stop offset="0" stop-color="#abd036"/><stop offset="1" stop-color="#34a6d7"/></linearGradient></defs>
    <rect x="0" y="0" width="1200" height="8" fill="url(#ctaBand)"/>
    <rect x="0" y="8" width="1200" height="10" fill="#fff"/>
  </svg>
</section>

<div class="abs" style="left:0;width:1200px;top:4282px;text-align:center;font-size:18px;font-weight:500;color:#3a3a3a">GuideLink Hub</div>

<div class="abs footer-note" style="left:212px">© 2018 GuideLinkHub. All Rights Reserved.</div>
<div class="abs footer-note" style="left:731px">Sign up is free, obligation free and 100% confidential.</div>

</body>
</html>
```